Manufacturing company needs new business card.

I need a unique Business Card that will truly stand out. Nothing too busy. Simple is good, right? Not looking for a standard design either. No cookie cutter layout. I am just looking for something interesting and a bit different. Does't have to completely off the wall crazy, just not your run of the mill business card. Clean and modern with a touch of industrial.

Target Market(s)

Air conditioning industry, Architects, builders.

Industry/Entity Type

Business

Contact Information for Business Card

Details to be included on card are:

Peter Vance
Managing Director

T: 1300 847 519
M: 0428 593 174
W: www.brenvaleworks.com.au
E: peter.vance@brenvaleworks.com.au
A: 58 Harwick Lane, Sydney NSW 2000

Font styles to use
Sans Serif

Colors
0355a3
848484
fbfbfb

Requirements
Must have
• Card design must be landscape.

```html
<!DOCTYPE html>
<html lang="en">
<head>
<meta charset="utf-8">
<title>Brenvale Works – Business Card</title>
<link href="https://fonts.googleapis.com/css2?family=Source+Sans+3:wght@400;600&display=swap" rel="stylesheet">
<style>
  :root {
    --stage: #000000;
    --card-blue: #1f4fa0;
    --ink-light: #fbfbfb;
    --card-radius: 62px;
  }
  * { margin: 0; padding: 0; box-sizing: border-box; }
  html, body {
    width: 1200px;
    height: 900px;
    overflow: hidden;
    background: var(--stage);
  }
  .canvas {
    position: relative;
    width: 1200px;
    height: 900px;
    font-family: "Source Sans 3", "Myriad Pro", sans-serif;
    color: var(--ink-light);
  }
  .card {
    position: absolute;
    top: 275px;
    width: 477px;
    height: 294px;
    background: var(--card-blue);
  }
  .card--back {
    left: 116px;
    border-radius: 0 var(--card-radius) 0 var(--card-radius);
  }
  .card--front {
    left: 622px;
    border-radius: var(--card-radius) 0 var(--card-radius) 0;
    display: flex;
    align-items: center;
    justify-content: center;
    padding-bottom: 14px;
  }
  .contact {
    position: absolute;
    left: 0;
    width: 477px;
    text-align: center;
  }
  .contact__name {
    top: 56px;
    font-weight: 600;
    font-size: 18px;
    line-height: 22px;
  }
  .contact__role {
    top: 77px;
    font-size: 13.5px;
    line-height: 18px;
  }
  .contact__details {
    top: 122px;
    list-style: none;
    font-size: 13.5px;
    line-height: 20px;
  }
  .contact__address {
    top: 212px;
    font-size: 13.5px;
    line-height: 18px;
  }
  .brand {
    display: flex;
    align-items: center;
    gap: 16px;
  }
  .brand__square {
    width: 34px;
    height: 34px;
    background: var(--ink-light);
    border-radius: 4px;
  }
  .brand__name {
    font-weight: 400;
    font-size: 26px;
    letter-spacing: 0.2px;
  }
</style>
</head>
<body>
  <main class="canvas">
    <section class="card card--back" aria-label="Card back with contact details">
      <p class="contact contact__name">Peter Vance</p>
      <p class="contact contact__role">Managing Director</p>
      <ul class="contact contact__details">
        <li>1300 847 519</li>
        <li>0428 593 174</li>
        <li>www.brenvaleworks.com.au</li>
        <li>peter.vance@brenvaleworks.com.au</li>
      </ul>
      <p class="contact contact__address">58 Harwick Lane, Sydney NSW 2000</p>
    </section>

    <section class="card card--front" aria-label="Card front with company name">
      <div class="brand">
        <span class="brand__square" aria-hidden="true"></span>
        <span class="brand__name">Brenvale Works</span>
      </div>
    </section>
  </main>
</body>
</html>
```